Dynamic Lead Design (Partial WebPage)

To encourage visitors to our website to donate to our organization, we would like to replace the Dynamic Lead on our website with one that will evoke emotion from the viewer and motivate them to donate generously.

The deliverable should be a mockup of the design in context of the current website. See attached file for editable area. Fonts used in the mockup should be code-able in HTML/CSS.

The website
http://www.hopelark.org

Please use this wireframe for reference:
http://app.mockvane.com/8b1c47e20f93d5a6c71e04b28d9a3f5e17c6b0d2/7315824

Content:
[Image should evoke emotion from the viewer and motivate them to donate generously.]
Headline - “Give to TIDEL.”
Sub Headline - “Cancer patients find answers here. Your donation makes that possible.”
Call to action label - “Donate”

We love these examples:

Bright Oak Harvest Drive (http://www.hd.brightoak.org/brightoak/v/index.jsp?vgnextoid=7a5d3f81c2e9b460VgnVCM100000318274bdRCRD)
Well Meadow (http://www.wellmeadow.org/)

Design Size:
width: 971px
height: 300px

***see attached document for design area***

- Organization Background -

Our website receives over 40,000 unique visitors each month - mostly cancer patients and their family members seeking information about their disease. We would like to drive our visitors to donate to our nonprofit throughout late November and December (the majority of our donations from individuals come in during that time period).

We will be mailing an appeal letter to our database in mid-November. With this banner ad, we seek to complement that appeal. Some key messages from our appeal are:

- We focus on getting patients and their loved ones the best, most up-to-date information from trusted doctors who are leaders in cancer research – for free. We don’t sell a particular product or procedure. We simply arm them with the most current information so they can make the best decision for their own (or their loved one’s) care.

- What is the value of the support they or someone they know has received from our organization? Twenty-five dollars? One hundred dollars? One thousand? Can you even put an amount to it? Whatever it is, please consider making an end of year donation to this organization that has helped so many, comforted hundreds of thousands of patients and caretakers, and been there when needed.

- 2014 will be a year of growth. We just hired our first executive director. She is experienced in helping small nonprofits grow in size, revenue, and scope, and will undoubtedly bring a new level of energy to our work.

- In just a few months, we will hold two patient forums – first-of-its-kind programs for the organization. As we continue to grow, we will be able to offer more of these types of programs to more patients throughout the US.

Industry/Entity Type

Charity

Requirements
Must have
• - Must Adhere to existing website branding

```html
<!DOCTYPE html>
<html lang="en">
<head>
<meta charset="utf-8">
<title>TIDEL — Give to TIDEL</title>
<link rel="stylesheet" href="https://fonts.googleapis.com/css2?family=Montserrat:wght@400;600;700&family=Arimo:wght@400;700&display=swap">
<style>
:root{
  --mint:#72cfa9;
  --mint-light:#e4f5ee;
  --salmon:#f09a8a;
  --slate:#6e6e6e;
  --link:#1c8a3c;
  --ink:#222;
  --muted:#666;
  --rule:#d9d9d9;
  --paper:#fff;
}
*{box-sizing:border-box;margin:0;padding:0}
html,body{width:1200px;height:783px;overflow:hidden;background:var(--paper)}
body{position:relative;font-family:"Arimo",Arial,sans-serif;color:var(--ink)}
.abs{position:absolute}

.brand{left:190px;top:34px;display:flex;align-items:center;gap:12px}
.brand-dot{width:70px;height:70px;border-radius:50%;background:var(--salmon)}
.brand-name{font-family:"Montserrat",sans-serif;font-weight:700;font-size:34px;color:var(--mint);letter-spacing:2px}

.search{left:579px;top:42px;width:364px;height:53px;border:6px solid var(--mint-light);border-radius:27px;background:var(--paper);box-shadow:0 2px 0 #d6efe4}
.search-input{left:19px;top:9px;width:253px;height:23px;border:1px solid #bcd;font-size:8px;color:#888;padding:6px 4px;background:#fff}
.search-btn{left:276px;top:9px;width:53px;height:23px;background:var(--mint-light);font-size:10px;font-weight:700;display:flex;align-items:center;justify-content:center;border:1px solid #cfe9dd}
.search-close{left:337px;top:10px;font-size:12px;color:#999}

.nav{top:138px;height:41px;display:flex;align-items:center;justify-content:center;text-align:center;font-family:"Montserrat",sans-serif;font-weight:600;color:#fff;font-size:14px;letter-spacing:1px;line-height:1.05;text-transform:uppercase}
.nav.two{font-size:13px}
.nav.two small{font-size:11.5px;display:block}
.nav-main{background:var(--mint)}
.nav-account{background:var(--slate)}
.nav-donate{background:var(--salmon)}
.donate-tab{left:1016px;top:105px;width:51px;height:40px;background:var(--salmon);border-radius:26px 12px 0 0}

.hero{left:190px;top:185px;width:877px;height:272px;background:linear-gradient(90deg,#f7dede 0%,#fbecea 45%,#fdf3f1 100%)}
.hero-photo{left:0;top:0;width:340px;height:272px;background:linear-gradient(90deg,#e9e4e6 0%,#d8cfd4 40%,#efe6e6 100%)}
.hero-rule{left:362px;width:463px;height:1px;background:var(--mint)}
.hero-title{left:352px;top:47px;width:483px;text-align:center;font-family:"Montserrat",sans-serif;font-weight:600;font-size:51px;letter-spacing:6px;color:var(--mint)}
.hero-sub{left:352px;top:132px;width:483px;text-align:center;font-family:"Montserrat",sans-serif;font-size:13px;letter-spacing:2.2px;color:#7b7474;line-height:17px;text-transform:uppercase}
.hero-cta{left:504px;top:183px;width:177px;height:46px;background:var(--salmon);border-radius:6px;display:flex;align-items:center;justify-content:center;gap:10px;font-family:"Montserrat",sans-serif;font-weight:700;font-size:17px;letter-spacing:4px;color:#fff}

.social{top:470px;width:27px;height:27px;border-radius:4px}
.share{left:619px;top:495px;width:179px;height:16px;border:1px solid #e08a88;border-radius:2px;font-size:11px;display:flex;align-items:center;gap:3px;padding-left:3px;background:#fff}
.share i{width:10px;height:10px;background:#8aa3cc;display:inline-block}

.section-title{left:189px;top:507px;font-size:16px;font-weight:700;color:var(--muted)}
.post-title{left:190px;width:625px;font-size:15.6px;font-weight:700;color:var(--link);line-height:18px}
.byline{left:190px;top:623px;font-size:12px;color:var(--ink)}
.byline b{font-weight:700}
.byline a{color:var(--link);font-weight:700;text-decoration:none}
.excerpt{left:190px;top:657px;width:620px;font-size:13.6px;line-height:18.5px}
.excerpt em{color:var(--link)}
.divider{left:190px;top:737px;width:622px;height:1px;background:var(--rule)}

.pill{left:835px;width:219px;height:41px;background:var(--salmon);box-shadow:0 1px 2px rgba(0,0,0,.2)}
.ask{top:519px;display:flex;align-items:center;gap:4px;padding-left:8px;font-family:"Montserrat",sans-serif;font-size:18px;color:#fff;letter-spacing:1px}
.qa{width:30px;height:30px;border-radius:50%;background:#7b7474;color:#fff;font-size:12px;display:flex;align-items:center;justify-content:center}
.forum{top:686px;text-align:center;color:#fff;font-family:"Montserrat",sans-serif;font-size:16px;letter-spacing:1px;line-height:18px;padding-top:3px}
.side-title{left:834px;top:584px;font-size:16.5px;font-weight:700;color:#555}
.side-link{left:835px;font-size:12px;font-weight:700;color:var(--link)}
</style>
</head>
<body>

<header>
  <div class="abs brand"><span class="brand-dot"></span><span class="brand-name">TIDEL</span></div>

  <div class="abs search">
    <div class="abs search-input">Site Custom Search</div>
    <div class="abs search-btn">Search</div>
    <div class="abs search-close">✕</div>
  </div>

  <nav>
    <div class="abs donate-tab">
      <svg width="51" height="34" viewBox="0 0 51 34"><circle cx="30" cy="17" r="9" fill="#fff"/><path d="M30 12v10M25 17h10" stroke="#3cc45a" stroke-width="3"/></svg>
    </div>
    <div class="abs nav nav-main" style="left:190px;width:151px">About TIDEL</div>
    <div class="abs nav nav-main two" style="left:345px;width:152px"><span>Ask Us<small>Discussion Forums</small></span></div>
    <div class="abs nav nav-main two" style="left:500px;width:154px"><span>General<br>Cancer Info</span></div>
    <div class="abs nav nav-main two" style="left:657px;width:153px"><span>Focused<br>Cancer Info</span></div>
    <div class="abs nav nav-account" style="left:814px;width:125px">Sign In | Join</div>
    <div class="abs nav nav-donate" style="left:942px;width:125px">Donate</div>
  </nav>
</header>

<section class="abs hero">
  <div class="abs hero-photo" role="img" aria-label="Photograph of a mother warmly hugging her young child in a bright room"></div>
  <div class="abs hero-rule" style="top:42px"></div>
  <h1 class="abs hero-title">GIVE TO TIDEL</h1>
  <div class="abs hero-rule" style="top:109px"></div>
  <p class="abs hero-sub">Cancer patients find answers here.<br>Your donation makes that possible.</p>
  <div class="abs hero-cta">
    <svg width="22" height="22" viewBox="0 0 22 22"><circle cx="11" cy="11" r="10" fill="#fff"/><path d="M11 6v10M6 11h10" stroke="#3cc45a" stroke-width="3"/></svg>
    DONATE
  </div>
</section>

<main>
  <div class="abs share"><i></i><i></i><i></i><i></i><span>Share/Email/More</span></div>
  <h2 class="abs section-title">Recent TIDEL News &amp; Posts</h2>

  <h3 class="abs post-title" style="top:567px">Cancer Care In Crisis? The Council on Care Quality's Report: Building<br>Better Oncology Care: Mapping a Fresh Path For a Strained System; Part I:<br>Where We Stand Today</h3>
  <p class="abs byline">by <b>Dr. Halvorsen</b> &nbsp;on &nbsp;Nov 10, 2013 &nbsp;in &nbsp;<a>TIDEL :: Cancer Basics</a></p>
  <p class="abs excerpt">&nbsp;A few months ago, the Council on Care Quality released the prepublication proofs of a massive report on the state of oncology care, saying that it was in crisis in the United States. I learned about it from an email that focused on the crisis part of the title. I was bo... &nbsp;<em>(Read More)</em></p>
  <div class="abs divider"></div>
  <h3 class="abs post-title" style="top:762px">Is there a place for live educational meetings in our new online world? Would</h3>
</main>

<aside>
  <span class="abs social" style="left:857px;background:#3b5a9a"></span>
  <span class="abs social" style="left:906px;background:#5fc3ea"></span>
  <span class="abs social" style="left:956px;background:#c9302c"></span>
  <span class="abs social" style="left:1004px;background:#f58a2c"></span>

  <div class="abs pill ask"><span class="qa">Q:</span><span class="qa">A:</span><span style="margin-left:14px">Ask Us</span></div>
  <h2 class="abs side-title">Welcome To TIDEL!</h2>
  <a class="abs side-link" style="top:610px">How To Use TIDEL</a>
  <a class="abs side-link" style="top:630px">General Cancer FAQs</a>
  <a class="abs side-link" style="top:654px">Recent TIDEL Site Post Comments</a>
  <div class="abs pill forum">TIDEL<br>Discussion Forums</div>
  <a class="abs side-link" style="top:738px">TIDEL Discussion Forum Guidelines</a>
  <a class="abs side-link" style="top:763px">Recent TIDEL Forum Activity</a>
</aside>

</body>
</html>
```